Gutschein-Design zur Pflegeberatung
Zielgruppe
Wir feiern mit unserem Pflegedienst das 10 Jährige Jubiläum. Da es wegen der Corona Pandemie keine Feierlichkeiten geben kann, würde ich wir einen Gutschein für eine kostenlose Pflegeberatung erstellen lassen. Auf die Vorderseite bitte den Gutschein mit dem Text:
Bilder bitte aus den öffentlichen Portalen verwenden.
Gutschein zur Pflegeberatung
Wir unterstützen bei der Beantragung eines Pflegegrades und helfen bei abgelehnten Anträgen.
Gerne informieren wir Sie über umfangreiche Möglichkeiten der ambulante Pflege und erstellen einen individuellen Versorgungsplan. Darüber hinaus erhalte Sie praktische Tipps zu Alltagshilfen und konkrete Hilfestellungen rund um die Pflege, damit Sie noch so lange wie möglich zu
Hause bleiben können.
Unten bitte einfügen: Gutschein gültig bis einschließlich Juli 2022
Auf die Rückseite bitte eine kurze Info zu unserem 10 Jährigen bestehen.
Vielleicht vielleicht wieder mit dem Slogan, Seit 10 Jahren rund um die Uhr für Sie im Einsatz.
Aufgabenstellung
Da wir zwei ambulante Filialen betreiben, muss das Logo auf die zweite Filiale angepasst werden.
Der Text und die Informationen bleiben jedoch gleich. Der Gutschein sollte sofort auffallen und animieren, im Pflegedienst anzurufen.

```html
<!DOCTYPE html>
<html lang="de">
<head>
<meta charset="utf-8">
<title>Gutschein zur Pflegeberatung</title>
<link href="https://fonts.googleapis.com/css2?family=Jost:wght@300;400;500&family=Poppins:ital,wght@0,700;0,800;1,700;1,800&display=swap" rel="stylesheet">
<style>
  :root {
    --yellow: #f2cb4e;
    --teal: #1fa9b0;
    --teal-light: #2bb8c2;
    --white: #ffffff;
    --ink: #1d1d1d;
    --stage: #d6d6d6;
    --skin: #e9c4a8;
    --scrubs: #1ec3cf;
  }
  * { box-sizing: border-box; margin: 0; padding: 0; }
  html, body { width: 1200px; height: 800px; overflow: hidden; }
  body {
    background: var(--stage);
    font-family: "Jost", sans-serif;
    position: relative;
  }
  .card {
    position: absolute;
    left: 280px;
    width: 640px;
    height: 372px;
    overflow: hidden;
    box-shadow: 0 6px 18px rgba(0,0,0,.18);
  }
  .card--front { top: 16px; background: var(--yellow); }
  .card--back { top: 408px; background: var(--white); }

  .heading {
    font-family: "Poppins", sans-serif;
    font-weight: 800;
    font-style: italic;
  }
  .photo {
    position: absolute;
    background: linear-gradient(180deg, var(--skin) 0%, var(--skin) 38%, var(--scrubs) 40%, var(--scrubs) 100%);
    border-radius: 110px 110px 0 0;
  }

  /* front */
  .front__photo { left: 270px; top: 36px; width: 200px; height: 336px; }
  .call { position: absolute; text-align: center; color: var(--teal); }
  .call__icon { display: block; margin: 0 auto 4px; }
  .call__title { font-size: 16px; line-height: 1.1; }
  .call__tel { font-family: "Poppins", sans-serif; font-style: italic; font-weight: 700; font-size: 11px; margin-top: 3px; }
  .front__call { left: 140px; top: 22px; width: 170px; }

  .title-band {
    position: absolute;
    background: var(--white);
    color: var(--teal);
    line-height: 1;
    white-space: nowrap;
  }
  .front__title {
    left: 0; top: 152px;
    font-size: 24px;
    padding: 9px 16px 9px 20px;
  }

  .service-list {
    position: absolute;
    left: 20px; top: 200px;
    width: 310px;
    background: var(--teal-light);
    color: var(--white);
    list-style: none;
    font-size: 15px;
    line-height: 1.3;
    padding: 8px 14px;
  }
  .service-list li::before { content: "→ "; }

  .slogan-block {
    position: absolute;
    right: -14px; top: 92px;
    width: 186px;
    background: var(--teal);
    color: var(--white);
    font-family: "Poppins", sans-serif;
    font-weight: 800;
    font-size: 16px;
    line-height: 1.2;
    text-transform: uppercase;
    letter-spacing: .04em;
    padding: 10px 14px 12px 16px;
    transform: rotate(-4deg);
  }
  .info-band {
    position: absolute;
    left: 250px; right: 0; top: 300px;
    background: var(--teal-light);
    color: var(--white);
    font-size: 14px;
    line-height: 1.3;
    padding: 8px 16px;
  }

  /* back */
  .logo-box {
    position: absolute;
    left: 22px; top: 20px;
    width: 104px; height: 58px;
    background: var(--teal);
    color: var(--white);
    font-weight: 300;
    font-size: 17px;
    letter-spacing: .1em;
    line-height: 1.05;
    display: flex; align-items: center; justify-content: center; text-align: center;
  }
  .back__intro {
    position: absolute;
    left: 160px; top: 26px; width: 460px;
    font-size: 14px;
    line-height: 1.35;
    color: var(--ink);
  }
  .back__band {
    position: absolute;
    left: 0; top: 88px; width: 640px; height: 212px;
    background: var(--yellow);
    clip-path: polygon(0 8%, 100% 0, 100% 86%, 0 100%);
  }
  .back__celebrate {
    position: absolute;
    left: 22px; top: 104px;
    font-size: 19px;
    color: var(--ink);
  }
  .back__title { left: 0; top: 134px; font-size: 22px; padding: 7px 14px 7px 22px; }
  .back__body {
    position: absolute;
    left: 22px; top: 178px; width: 390px;
    font-size: 12.5px;
    line-height: 1.3;
    color: var(--ink);
  }
  .slogan-box {
    position: absolute;
    left: 420px; top: 116px; width: 200px;
    background: var(--white);
    color: var(--teal);
    font-family: "Poppins", sans-serif;
    font-weight: 700;
    font-style: italic;
    font-size: 13px;
    line-height: 1.25;
    padding: 8px 12px;
  }
  .seal { position: absolute; left: 560px; top: 78px; }
  .back__photo { left: 440px; top: 190px; width: 180px; height: 182px; }
  .address {
    position: absolute;
    left: 22px; top: 304px;
    font-size: 12px;
    line-height: 1.3;
    color: var(--ink);
  }
  .address__name { font-weight: 500; }
  .address__web { text-decoration: underline; }
  .back__call { left: 196px; top: 300px; width: 110px; }
  .back__call .call__title { font-size: 13px; }
  .hours {
    position: absolute;
    left: 316px; top: 304px;
    font-size: 12px;
    line-height: 1.3;
    color: var(--ink);
  }
  .hours__label { font-weight: 500; text-decoration: underline; }
</style>
</head>
<body>

<section class="card card--front" aria-label="Gutschein Vorderseite">
  <div class="photo front__photo" role="img" aria-label="Foto einer lächelnden Pflegerin in türkiser Kleidung, Daumen hoch"></div>

  <div class="call front__call">
    <svg class="call__icon" width="38" height="38" viewBox="0 0 38 38" aria-hidden="true">
      <circle cx="19" cy="19" r="19" fill="var(--teal)"/>
      <path d="M13 11c1-1 2.5-1 3 .2l1.4 3c.3.7.1 1.4-.5 1.9l-1.2 1c.9 2 2.4 3.6 4.3 4.6l1.1-1.2c.5-.6 1.3-.7 2-.4l3 1.5c1.1.5 1.1 2 .1 3l-1 1c-1.3 1.3-4 1.2-7-1s-5.6-5.6-6-8.4c-.3-2 .3-3.7 1.3-4.6z" fill="var(--white)"/>
    </svg>
    <div class="call__title heading">Jetzt Termin<br>vereinbaren!</div>
    <div class="call__tel">Tel.: 030-7654321</div>
  </div>

  <div class="slogan-block">Seit 10 Jahren<br>rund um die<br>Uhr für Sie<br>im Einsatz!</div>

  <div class="title-band heading front__title">Gutschein zur Pflegeberatung</div>

  <ul class="service-list">
    <li>Beantragen eines Pflegegrades</li>
    <li>Hilfe bei abgelehnten Anträgen</li>
    <li>Individueller Versorgungsplan</li>
  </ul>

  <p class="info-band">Inklusive weiteren Informationen zu Möglichkeiten der ambulanten Pflege &amp; praktischen Hilfestellungen</p>
</section>

<section class="card card--back" aria-label="Gutschein Rückseite">
  <div class="back__band"></div>

  <div class="logo-box">IHR<br>LOGO</div>

  <p class="back__intro">Vereinbaren Sie jetzt Ihren Termin zur kostenfreien Pflegeberatung!<br>Der Gutschein ist bis einschließlich Juli 2022 gültig.</p>

  <div class="back__celebrate heading">Wir feiern 10 jähriges Jubiläum!</div>
  <div class="title-band heading back__title">Gutschein zur Pflegeberatung</div>

  <p class="back__body">Wir unterstützen bei der Beantragung eines Pflegegrades und helfen bei abgelehnten Anträgen. Gerne informieren wir Sie über umfangreiche Möglichkeiten der ambulante Pflege und erstellen einen individuellen Versorgungsplan. Darüber hinaus erhalte Sie praktische Tipps zu Alltagshilfen und konkrete Hilfestellungen rund um die Pflege, damit Sie noch so lange wie möglich zu Hause bleiben können.</p>

  <svg class="seal" width="44" height="44" viewBox="0 0 44 44" aria-hidden="true">
    <circle cx="22" cy="22" r="20" fill="var(--yellow)"/>
  </svg>
  <p class="slogan-box">Seit 10 Jahren sind wir rund um die Uhr für Sie im Einsatz.</p>

  <div class="photo back__photo" role="img" aria-label="Foto einer Pflegerin mit Stethoskop und roter Mappe"></div>

  <div class="address">
    <div class="address__name">Pflegedienst RAVOLUTEK<br>Standort Stadtteil</div>
    <div>Straße&nbsp;•&nbsp;PLZ &amp; ORT</div>
    <div class="address__web">www.pflege-am-ort.de</div>
  </div>

  <div class="call back__call">
    <svg class="call__icon" width="28" height="28" viewBox="0 0 38 38" aria-hidden="true">
      <circle cx="19" cy="19" r="19" fill="var(--teal)"/>
      <path d="M13 11c1-1 2.5-1 3 .2l1.4 3c.3.7.1 1.4-.5 1.9l-1.2 1c.9 2 2.4 3.6 4.3 4.6l1.1-1.2c.5-.6 1.3-.7 2-.4l3 1.5c1.1.5 1.1 2 .1 3l-1 1c-1.3 1.3-4 1.2-7-1s-5.6-5.6-6-8.4c-.3-2 .3-3.7 1.3-4.6z" fill="var(--white)"/>
    </svg>
    <div class="call__title heading">Jetzt Termin<br>vereinbaren!</div>
  </div>

  <div class="hours">
    <div class="hours__label">Bürozeiten:</div>
    <div>Montag-Freitag: ... Uhr</div>
    <div>Samstag: ...Uhr</div>
    <div>Tel.: 030-7654321</div>
  </div>
</section>

</body>
</html>
```